Business Card Design

Retail Do It Yourself Studio/Store
I sell Lena Pruitt Velvet Paint and supplies to repurpose furniture. Classes are held to teach basic chalk paint techniques. Lena Pruitt Easy Coat Paint does not require sanding or primer. It is not only perfect for furniture but Kitchen and Bathroom cabinets. Other classes include painting with laquer,painting with milk paint, antiquing mirrors, using zinc on stainless steel. Painting on fabric, upholstery, repurposing garage sale finds. Taking your $5 dollar item and turning it into a one of kind interior design masterpiece. Studio time is also sold. Patrons may come for a one time visit and use our paint and supplies to repurpose their furniture or they may want a membership to come anytime they want to use our supplies to work on their pieces. I will also consign repurposed pieces in the store, at local antique markets and online.

Industry/Entity Type

Painting

Contact Information for Business Card

Joan Tevis
418 Corwin Blvd. Suite 207
Bellmere Cove, Westhaven 32971
321-555-0164
https://www.facebook.com/tinderwickloftstudio

```html
<!DOCTYPE html>
<html lang="en">
<head>
<meta charset="utf-8">
<title>Tinderwick Loft Studio – Business Cards</title>
<link rel="stylesheet" href="https://fonts.googleapis.com/css2?family=Cinzel:wght@500&family=Cormorant+Garamond:wght@500&family=Pinyon+Script&family=Open+Sans:wght@400&display=swap">
<style>
  :root {
    --backdrop: #3a3431;
    --card-dark: #6a6a6a;
    --card-light: #f8f8f6;
    --ink: #1c1c1c;
    --paper-text: #ffffff;
    --contact-band: #5f5f5f;
    --social-band: #1d1a19;
    --rule: #8a8a8a;
  }
  * { margin: 0; padding: 0; box-sizing: border-box; }
  html, body { width: 1200px; height: 768px; overflow: hidden; }
  body {
    background: var(--backdrop);
    position: relative;
    font-family: "Open Sans", sans-serif;
  }
  .card {
    position: absolute;
    top: 234px;
    width: 520px;
    height: 300px;
    overflow: hidden;
    box-shadow: 0 10px 28px rgba(0,0,0,.45);
  }
  .card--front { left: 50px; background: var(--card-dark); color: var(--paper-text); }
  .card--back { left: 630px; background: var(--card-light); color: var(--ink); }

  .brand {
    position: absolute;
    left: 0; right: 0;
    text-align: center;
  }
  .brand__name {
    font-family: "Cinzel", serif;
    font-weight: 500;
    font-size: 25px;
    letter-spacing: 1px;
  }
  .brand__tagline {
    font-family: "Open Sans", sans-serif;
    font-weight: 400;
    font-size: 14px;
    letter-spacing: 0.5px;
    margin-top: 8px;
  }
  .card--front .brand { top: 48px; }
  .card--back .brand { top: 58px; }

  .photo-strip {
    position: absolute;
    left: 0; right: 0; bottom: 0;
    height: 118px;
    background: linear-gradient(90deg,
      #2fa7ad 0%, #3bb3b4 14%, #c9c3b8 22%, #e9e6df 38%,
      #a5683a 48%, #d9c23c 58%, #e8d85a 64%,
      #7fa7c2 76%, #9a6a44 88%, #7a4e30 100%);
  }

  .holder {
    position: absolute;
    top: 160px;
    left: 110px; right: 110px;
    display: flex;
    align-items: center;
    gap: 12px;
  }
  .holder__rule { flex: 1; height: 1px; background: var(--rule); }
  .holder__name {
    font-family: "Pinyon Script", cursive;
    font-size: 30px;
    line-height: 1.2;
  }

  .contact {
    position: absolute;
    left: 0; bottom: 0;
    width: 300px;
    height: 92px;
    background: var(--contact-band);
    color: var(--paper-text);
    font-size: 12.5px;
    line-height: 1.45;
    padding: 12px 0 0 18px;
  }
  .contact__row { display: flex; gap: 9px; align-items: flex-start; }
  .contact__icon { width: 12px; height: 14px; flex: none; margin-top: 2px; }
  .contact__lines { display: block; }

  .social {
    position: absolute;
    right: 0; bottom: 0;
    width: 220px;
    height: 44px;
    background: var(--social-band);
    color: var(--paper-text);
    font-size: 14px;
    display: flex;
    align-items: center;
    gap: 8px;
    padding-left: 20px;
  }
  .social__mark { width: 12px; height: 12px; background: var(--paper-text); flex: none; }
</style>
</head>
<body>

  <section class="card card--front">
    <div class="brand">
      <div class="brand__name">Tinderwick Loft Studio</div>
      <div class="brand__tagline">Every Piece - Renewed</div>
    </div>
    <div class="photo-strip" role="img" aria-label="Photo strip of repurposed painted furniture: teal bench, white cabinets, yellow table and blue chairs in the studio"></div>
  </section>

  <section class="card card--back">
    <div class="brand">
      <div class="brand__name">Tinderwick Loft Studio</div>
      <div class="brand__tagline">Every Piece - Renewed</div>
    </div>

    <div class="holder">
      <span class="holder__rule"></span>
      <span class="holder__name">Joan Tevis</span>
      <span class="holder__rule"></span>
    </div>

    <div class="contact">
      <div class="contact__row">
        <svg class="contact__icon" viewBox="0 0 12 14" aria-hidden="true"><path d="M2 2h2l1 3-1.5 1a7 7 0 0 0 3.5 3.5L8 8l3 1v2c0 1-1 1.5-2 1.5A9 9 0 0 1 .5 4C.5 3 1 2 2 2z" fill="#fff"/></svg>
        <span>+1 555-555-0164</span>
      </div>
      <div class="contact__row">
        <svg class="contact__icon" viewBox="0 0 12 14" aria-hidden="true"><path d="M6 .5a4.5 4.5 0 0 0-4.5 4.5C1.5 8.5 6 13.5 6 13.5s4.5-5 4.5-8.5A4.5 4.5 0 0 0 6 .5zm0 6.3a1.8 1.8 0 1 1 0-3.6 1.8 1.8 0 0 1 0 3.6z" fill="#fff"/></svg>
        <span class="contact__lines">418 Corwin Blvd. Suite 207<br>Bellmere Cove, Westhaven 30471</span>
      </div>
    </div>

    <div class="social">
      <span class="social__mark" aria-hidden="true"></span>
      <span>/tinderwickloftstudio</span>
    </div>
  </section>

</body>
</html>
```